TARO PTY LTD - Business Cards

Design a modern business card - using the attached Designs.
Same design as on the front, apart from the names/numbers/emails to be different.
We want the cards to be very glossy to stand out, do I think the simple black/white/metallic will be effective.
Both lots of details below:

Lyle Marrick
Director
lyle_taro@quintmail.example
0493 628 304

Simon Prowle
Director
simon_taro@quintmail.example
0438 514 209

```html
<!DOCTYPE html>
<html lang="en">
<head>
<meta charset="utf-8">
<title>TARO PTY LTD – Business Cards</title>
<link href="https://fonts.googleapis.com/css2?family=Bitter:wght@400;700&display=swap" rel="stylesheet">
<style>
  :root {
    --page-bg: #e9e7e4;
    --card-white: #ffffff;
    --charcoal: #2b3338;
    --swoosh-grey: #b9bcbe;
    --text-light: #ffffff;
    --metal-dark: #9c9ea3;
    --metal-mid: #c9cacd;
    --metal-light: #f4f4f5;
    --brand-dark: #2f3438;
  }
  * { box-sizing: border-box; margin: 0; padding: 0; }
  html, body { width: 1200px; height: 475px; overflow: hidden; }
  body {
    background: var(--page-bg);
    font-family: "Bitter", Georgia, serif;
    position: relative;
  }
  .card {
    position: absolute;
    top: 85px;
    width: 520px;
    height: 305px;
    overflow: hidden;
    box-shadow: 0 6px 18px rgba(0,0,0,0.25);
  }
  .card--front { left: 50px; background: var(--card-white); }
  .card--back {
    left: 630px;
    background: linear-gradient(100deg,
      var(--metal-mid) 0%, var(--metal-light) 18%, var(--metal-dark) 40%,
      var(--metal-light) 62%, var(--metal-mid) 80%, var(--metal-dark) 100%);
  }
  .card__band { position: absolute; inset: 0; width: 100%; height: 100%; }
  .brand {
    position: absolute;
    left: 0; right: 0;
    display: flex;
    align-items: center;
    justify-content: center;
    gap: 10px;
    color: var(--brand-dark);
    font-weight: 700;
    letter-spacing: 0.06em;
  }
  .card--front .brand { top: 42px; font-size: 26px; }
  .card--back .brand { top: 125px; font-size: 38px; gap: 14px; }
  .brand__dot {
    width: 18px; height: 18px; border-radius: 50%;
    background: var(--brand-dark);
  }
  .card--back .brand__dot { width: 26px; height: 26px; }
  .contact {
    position: absolute;
    left: 0; right: 0; top: 196px;
    text-align: center;
    color: var(--text-light);
  }
  .contact__name { font-size: 19px; font-weight: 700; }
  .contact__role { font-size: 15px; font-weight: 400; }
  .contact__line {
    margin-top: 8px;
    font-size: 15px;
    display: flex;
    align-items: center;
    justify-content: center;
    gap: 7px;
  }
  .contact__line:first-of-type { margin-top: 10px; }
  .icon { width: 13px; height: 13px; fill: none; stroke: var(--text-light); stroke-width: 1.6; }
</style>
</head>
<body>
  <section class="card card--front" aria-label="Business card front">
    <svg class="card__band" viewBox="0 0 520 305" preserveAspectRatio="none" aria-hidden="true">
      <path d="M0,242 Q200,96 520,152" fill="none" stroke="var(--swoosh-grey)" stroke-width="6"/>
      <path d="M0,305 L0,255 Q200,110 520,165 L520,305 Z" fill="var(--charcoal)"/>
    </svg>
    <div class="brand"><span class="brand__dot"></span><span>TARO PTY LTD</span></div>
    <div class="contact">
      <p><span class="contact__name">Simon Prowle,</span> <span class="contact__role">Director</span></p>
      <p class="contact__line">
        <svg class="icon" viewBox="0 0 14 14" aria-hidden="true"><path d="M3,1 L5.5,1 L6.5,4 L5,5.2 Q6.3,8 9,9 L10.2,7.5 L13,8.5 L13,11 Q12,13 9.5,12.5 Q3,10.5 1.5,4.5 Q1,2 3,1 Z"/></svg>
        <span>0438 514 209</span>
      </p>
      <p class="contact__line">
        <svg class="icon" viewBox="0 0 14 14" aria-hidden="true"><rect x="1" y="3" width="12" height="8"/><path d="M1,3 L7,8 L13,3"/></svg>
        <span>simon_taro@quintmail.example</span>
      </p>
    </div>
  </section>

  <section class="card card--back" aria-label="Business card back">
    <div class="brand"><span class="brand__dot"></span><span>TARO PTY LTD</span></div>
  </section>
</body>
</html>
```